Store Front Sign for Vape Store

Interested in getting a store front sign graphic done. Sign is for over the door (lighted sign). Dimensions of sign: 6 feet long x 2 feet high.
Sign is for a Vape Store. I have attached the logo to be used.
Looking for a modern and professional look
Phone numbers to be used.
Whatsapp# 364-9105
Contact #593-6148
Sign should have Instagram & Facebook logos and. handle @mistralhaze

Industry/Entity Type

Vape | Electronic Cigarettes

Colors

Designer to choose colors to be used in the design.

Requirements
Must have
• Facebook and Instagram Logos. Contact Numbers.
Should not have
• Any Persons.

```html
<!DOCTYPE html>
<html lang="en">
<head>
<meta charset="utf-8">
<title>Mistral Haze – Storefront Sign</title>
<link href="https://fonts.googleapis.com/css2?family=Montserrat:wght@600&display=swap" rel="stylesheet">
<style>
  :root {
    --page: #eceeef;
    --sign-dark: #2a282a;
    --sign-edge: #111011;
    --band-start: #00ade6;
    --band-end: #0a80b4;
    --badge: #232223;
    --ring: #0a9ad8;
    --white: #ffffff;
  }
  * { margin: 0; padding: 0; box-sizing: border-box; }
  html, body {
    width: 1200px; height: 889px; overflow: hidden;
    background: var(--page);
    font-family: "Montserrat", sans-serif;
  }
  .sign {
    position: absolute; left: 30px; top: 254px;
    width: 1140px; height: 380px;
    background: var(--sign-dark);
    box-shadow: 0 0 0 4px var(--sign-edge);
    overflow: hidden;
  }
  .sign__texture {
    position: absolute; inset: 0;
    background: radial-gradient(ellipse at 50% 50%, #302d30 0%, var(--sign-dark) 70%);
  }
  .sign__band {
    position: absolute; left: 0; right: 0; top: 128px; height: 118px;
    background: linear-gradient(90deg, var(--band-start) 0%, var(--band-start) 45%, var(--band-end) 100%);
  }
  .contacts {
    position: absolute; left: 92px; top: 140px;
    display: flex; flex-direction: column; gap: 14px;
  }
  .contact {
    display: flex; align-items: center; gap: 18px;
    color: var(--white); font-size: 34px; letter-spacing: 1px;
  }
  .contact__icon {
    width: 40px; height: 40px; border-radius: 50%;
    background: var(--white);
    display: flex; align-items: center; justify-content: center;
  }
  .badge {
    position: absolute; left: 448px; top: 45px;
    width: 290px; height: 290px; border-radius: 50%;
    background: var(--badge);
    border: 6px solid var(--ring);
    box-shadow: 0 0 0 6px #1a191a;
    display: flex; align-items: center; justify-content: center;
    text-align: center;
  }
  .badge__name {
    color: var(--white); font-size: 46px; line-height: 1.05;
  }
  .social {
    position: absolute; right: 72px; top: 156px;
    display: flex; flex-direction: column; align-items: center; gap: 8px;
    color: var(--white);
  }
  .social__icons { display: flex; gap: 10px; }
  .social__icon {
    width: 26px; height: 26px; border-radius: 50%; background: var(--white);
  }
  .social__handle { font-size: 22px; letter-spacing: 0.5px; }
</style>
</head>
<body>
  <div class="sign">
    <div class="sign__texture" role="img" aria-label="Dark honeycomb hexagon pattern background"></div>
    <div class="sign__band"></div>

    <div class="contacts">
      <div class="contact">
        <span class="contact__icon">
          <svg width="22" height="22" viewBox="0 0 24 24" aria-hidden="true">
            <path fill="#00a9e2" d="M6.6 10.8a15.1 15.1 0 0 0 6.6 6.6l2.2-2.2a1 1 0 0 1 1-.25 11.4 11.4 0 0 0 3.6.57 1 1 0 0 1 1 1V20a1 1 0 0 1-1 1A17 17 0 0 1 3 4a1 1 0 0 1 1-1h3.5a1 1 0 0 1 1 1c0 1.25.2 2.45.57 3.57a1 1 0 0 1-.25 1z"/>
          </svg>
        </span>
        <span class="contact__number">593-6148</span>
      </div>
      <div class="contact">
        <span class="contact__icon"></span>
        <span class="contact__number">364-9105</span>
      </div>
    </div>

    <div class="badge">
      <span class="badge__name">Mistral<br>Haze</span>
    </div>

    <div class="social">
      <div class="social__icons">
        <span class="social__icon"></span>
        <span class="social__icon"></span>
      </div>
      <span class="social__handle">@mistralhaze</span>
    </div>
  </div>
</body>
</html>
```